professional business card

A Clean looking business card for a money transfer company. Our company is call Velorix= Transfer + Send = Transcend (next level)
to show professionalism as well as some effects to show digital tech.

1 side to have position, name and address
2 side to have company name and show that we provide money exchange and cross-border money transfer

Target Market(s)

Remittance companies and high net worth individuals

Industry/Entity Type

Finance

Contact Information for Business Card

Name, address, email, title, services- money exchange and cross-border remittance

Requirements
Nice to have
• Digital age feel

```html
<!DOCTYPE html>
<html lang="en">
<head>
<meta charset="utf-8">
<title>Velorix Business Card</title>
<link rel="stylesheet" href="https://fonts.googleapis.com/css2?family=Montserrat:wght@500;600&family=Poppins:wght@400&display=swap">
<style>
  :root {
    --ink: #263340;
    --cyan: #69d4e0;
    --cyan-faint: #eef9fa;
    --paper: #ffffff;
    --backdrop: #8a8a8a;
  }
  * { margin: 0; padding: 0; box-sizing: border-box; }
  html, body { width: 1093px; height: 1200px; overflow: hidden; background: var(--backdrop); }
  .canvas { position: relative; width: 1093px; height: 1200px; }

  .card {
    position: absolute;
    left: 265px;
    width: 578px;
    height: 357px;
    border-radius: 26px;
    overflow: hidden;
  }
  .card--front { top: 226px; background: var(--paper); }
  .card--back { top: 621px; background: var(--ink); }

  .brand-field {
    position: absolute;
    left: 0;
    top: 0;
    width: 302px;
    height: 100%;
    border-radius: 0 150px 150px 0;
  }
  .card--front .brand-field {
    background: linear-gradient(90deg, var(--cyan-faint) 0%, var(--cyan-faint) 55%, rgba(238, 249, 250, 0) 100%);
  }
  .card--back .brand-field {
    background: linear-gradient(135deg, var(--cyan) 0%, #4fb8c6 55%, #2f5a68 100%);
  }

  .brand {
    position: absolute;
    display: flex;
    align-items: center;
    gap: 14px;
    font-family: "Montserrat", sans-serif;
    font-weight: 500;
    letter-spacing: 1px;
    line-height: 1;
  }
  .brand__square { width: 34px; height: 34px; background: var(--cyan); }
  .card--front .brand { right: 33px; top: 68px; font-size: 47px; color: var(--ink); }
  .card--back .brand { left: 306px; top: 200px; font-size: 42px; color: var(--paper); }

  .person { position: absolute; left: 27px; top: 191px; }
  .person__name {
    font-family: "Montserrat", sans-serif;
    font-weight: 500;
    font-size: 25px;
    color: var(--ink);
    line-height: 1;
  }
  .person__title {
    font-family: "Poppins", sans-serif;
    font-size: 17px;
    color: var(--cyan);
    line-height: 1;
    margin-top: 3px;
  }

  .divider {
    position: absolute;
    left: 25px;
    top: 247px;
    width: 516px;
    height: 1px;
    background: var(--ink);
  }

  .contact, .address {
    position: absolute;
    font-family: "Poppins", sans-serif;
    font-size: 17px;
    color: var(--ink);
    line-height: 21px;
    list-style: none;
  }
  .contact { left: 27px; top: 264px; }
  .contact li { display: flex; align-items: center; gap: 7px; }
  .contact svg { width: 15px; height: 15px; flex: none; }
  .address { right: 33px; top: 285px; text-align: right; }

  .tagline {
    position: absolute;
    left: 300px;
    width: 236px;
    top: 286px;
    text-align: center;
    font-family: "Montserrat", sans-serif;
    font-weight: 500;
    font-size: 15px;
    line-height: 19px;
    color: var(--paper);
    white-space: nowrap;
  }
</style>
</head>
<body>
<main class="canvas">

  <section class="card card--front">
    <div class="brand-field" role="img" aria-label="Faint large brand mark decoration"></div>

    <div class="brand"><span class="brand__square"></span>VELORIX</div>

    <div class="person">
      <p class="person__name">DANIEL HARPER</p>
      <p class="person__title">Managing Director</p>
    </div>

    <div class="divider"></div>

    <ul class="contact">
      <li>
        <svg viewBox="0 0 16 16" aria-hidden="true"><path d="M4 1.5l2.3 3-1.4 1.6c.8 1.8 2.2 3.2 4 4l1.6-1.4 3 2.3-1.4 2.4C7 13.2 2.8 9 2.1 3.7z" fill="none" stroke="#263340" stroke-width="1.6" stroke-linejoin="round"/></svg>
        044-987 654 321
      </li>
      <li>
        <svg viewBox="0 0 16 16" aria-hidden="true"><rect x="1" y="3" width="14" height="10" fill="#263340"/><path d="M1 3l7 6 7-6" fill="none" stroke="#fff" stroke-width="1.2"/></svg>
        info@velorixpay.com
      </li>
      <li>
        <svg viewBox="0 0 16 16" aria-hidden="true"><g fill="none" stroke="#263340" stroke-width="1.3"><circle cx="8" cy="8" r="6.5"/><ellipse cx="8" cy="8" rx="3" ry="6.5"/><path d="M1.5 8h13M2.5 4.8h11M2.5 11.2h11"/></g></svg>
        www.velorixpay.com
      </li>
    </ul>

    <p class="address">421, Address line goes here<br>45452,Country Name</p>
  </section>

  <section class="card card--back">
    <div class="brand-field" role="img" aria-label="Large brand mark decoration in cyan"></div>
    <div class="brand">VELORIX</div>
    <p class="tagline">MONEY EXCHANGE AND<br>CROSS-BORDER REMITTANCE</p>
  </section>

</main>
</body>
</html>
```